依頼詳細
PCとスマホデザインの両方納品をいただきますが、
まずはデザインイメージが確認しやすいPCページのみの提案をお願いします。
スマホページは当選者に納品時にお願いしたいと思います。
スマホサイズは横幅750pxのサイズで作成してください。

レスポンシブウェブデザインを意識したデザインでお願いします。

デザインに関しては、添付してあるデザインレイアウト設計シートを基にお願いします。
参考サイトのURLはデザインレイアウト設計シートに記載してあります。

画像データについては、既存サイトや参考サイト、フリー素材から流用してイメージ画像に当て込んでください。
足りない場合は、一旦他のサイトの写真をサンプルとして入れてください。(サンプルなどの表記をお願いします)
ページ数
1ページ
希望イメージ
シンプル 複雑
単色 カラフル
暗い 明るい
日常 高級
遊び心 厳粛
未来的 伝統的
女性的 男性的
希望する色
青系、水色系、明るい色味
納品ファイル
• 高解像度JPG (.jpg)
• イラストレーター形式 (.ai)
• フォトショップ形式 (.psd)
• PNG形式 (.png)
補足説明
上記のいずれか1つ。アウトラインありとなしの2つ。

クライアントのイメージ通りでした。

たくさんのご提案ありがとうございました。
次回もぜひ、よろしくお願い致します。

```html
<!DOCTYPE html>
<html lang="ja">
<head>
<meta charset="utf-8">
<title>ルーチェ・プロダクツ</title>
<link href="https://fonts.googleapis.com/css2?family=Noto+Sans+JP:wght@400;500;700;900&display=swap" rel="stylesheet">
<style>
:root{
  --blue:#1cb4e3;
  --blue-dark:#0f9cc9;
  --ink:#333;
  --muted:#666;
  --gray-bg:#f0f0f0;
  --line:#d8d8d8;
  --yellow:#ffe33b;
  --red:#e8443a;
  --white:#fff;
}
*{box-sizing:border-box;margin:0;padding:0}
html,body{width:1200px;height:3144px;overflow:hidden}
body{font-family:"Noto Sans JP",sans-serif;color:var(--ink);background:var(--white);position:relative}
a{color:inherit;text-decoration:none}

/* header */
.site-header{position:absolute;top:0;left:0;width:1200px;height:120px;z-index:5}
.brand{position:absolute;left:40px;top:20px;width:150px;height:66px;background:var(--blue);color:var(--white);font-weight:900;font-size:34px;letter-spacing:3px;display:flex;align-items:center;justify-content:center;border-radius:8px}
.global-nav{position:absolute;left:290px;top:40px;display:flex;gap:36px;font-size:18px;font-weight:700}
.header-contact{position:absolute;right:16px;top:0;width:176px;height:150px;background:var(--blue);color:var(--white);display:flex;flex-direction:column;align-items:center;justify-content:center;gap:14px;font-size:17px;font-weight:700}

/* hero */
.hero{position:absolute;top:0;left:0;width:1200px;height:592px;overflow:hidden}
.hero-photo{position:absolute;left:0;top:0;width:1200px;height:592px;background:linear-gradient(120deg,#f4f6f6 0%,#e7ebea 45%,#d8dedd 70%,#c9ced0 100%)}
.hero-shape{position:absolute;left:0;top:0}
.hero-copy{position:absolute;left:40px;top:214px;color:var(--white)}
.hero-label{font-size:15px;font-weight:700;letter-spacing:2px;color:var(--white)}
.hero-title{margin-top:6px;font-size:40px;line-height:1.4;font-weight:900}
.hero-title span{background:var(--blue);padding:0 8px}
.hero-button{position:absolute;left:40px;top:384px;width:270px;height:62px;background:var(--white);color:var(--ink);font-size:18px;font-weight:700;display:flex;align-items:center;justify-content:center;border-radius:4px;box-shadow:0 3px 8px rgba(0,0,0,.15)}

/* section heading */
.section-title{font-size:38px;font-weight:900;display:flex;align-items:center;gap:16px}
.section-title::before{content:"";width:8px;height:46px;background:var(--blue)}
.section-title.small{font-size:30px}
.section-title.small::before{height:38px}

.btn{display:flex;align-items:center;justify-content:center;background:var(--blue);color:var(--white);font-weight:700;border-radius:4px}

/* products */
.products{position:absolute;top:640px;left:0;width:1200px;height:560px}
.products .section-title{position:absolute;left:100px;top:30px}
.products .btn{position:absolute;left:810px;top:0;width:300px;height:76px;font-size:20px}
.product-track{position:absolute;left:100px;top:130px;width:1000px;display:flex;gap:28px}
.product-card{width:228px}
.product-cat{display:flex;align-items:center;gap:8px;font-size:15px;font-weight:700;height:28px}
.product-cat i{width:16px;height:16px;background:var(--red);display:block;border-radius:2px}
.product-photo{position:relative;margin-top:6px;width:228px;height:228px}
.badge-new{position:absolute;left:0;top:0;background:var(--yellow);font-size:14px;font-weight:900;padding:4px 10px}
.product-name{margin-top:10px;font-size:15px;line-height:1.5;border-bottom:1px solid var(--line);padding-bottom:8px}
.arrow{position:absolute;top:250px;width:36px;height:66px}
.arrow.prev{left:40px}.arrow.next{right:40px}
.dots{position:absolute;top:502px;left:0;width:1200px;display:flex;justify-content:center;gap:14px}
.dots i{width:18px;height:18px;border-radius:50%;background:#444;display:block}
.dots i:first-child{background:var(--white);border:3px solid var(--blue)}

/* search */
.search{position:absolute;top:1222px;left:120px;width:960px;height:160px;background:var(--blue);padding:20px 28px;color:var(--white)}
.search h2{font-size:26px;font-weight:900;display:flex;align-items:center;gap:12px}
.search-row{margin-top:22px;display:flex;gap:14px}
.search-input{flex:1;height:56px;background:var(--white);color:#aaa;font-size:15px;display:flex;align-items:center;padding-left:20px}
.search-submit{width:240px;height:56px;background:var(--white);color:var(--ink);font-size:18px;font-weight:700;display:flex;align-items:center;justify-content:center}

/* news */
.news{position:absolute;top:1440px;left:0;width:1200px;height:320px;background:var(--gray-bg)}
.news .section-title{position:absolute;left:100px;top:60px}
.news-list{position:absolute;left:100px;top:150px;width:1000px;list-style:none}
.news-list li{display:flex;align-items:center;height:46px;font-size:15px;border-bottom:1px solid var(--line)}
.news-date{width:120px}
.news-tag{width:100px;height:28px;font-size:13px;font-weight:700;display:flex;align-items:center;justify-content:center;margin-right:28px}
.tag-info{background:var(--yellow)}
.tag-new{background:var(--blue);color:var(--white)}
.news-text{text-decoration:underline}

/* info columns */
.info{position:absolute;top:1800px;left:100px;width:1000px;display:flex;gap:34px}
.info-col{width:310px}
.info-photo{margin-top:24px;width:310px;height:206px}
.info-text{margin-top:18px;font-size:15px;line-height:1.7;height:58px}
.info-col .btn{margin-top:20px;width:250px;height:64px;font-size:17px;margin-left:30px}

/* contact */
.contact{position:absolute;top:2400px;left:0;width:1200px;height:320px;background:var(--gray-bg)}
.contact .section-title{position:absolute;left:100px;top:70px}
.contact-text{position:absolute;left:100px;top:150px;width:360px;font-size:15px;line-height:1.8}
.contact-links{position:absolute;left:496px;top:70px;display:flex;gap:36px}
.contact-links .btn{width:286px;height:170px;font-size:22px}

/* footer */
.site-footer{position:absolute;top:2760px;left:0;width:1200px;height:328px;background:var(--blue);color:var(--white)}
.footer-nav{position:absolute;top:36px;list-style:none;font-size:15px;line-height:2.5}
.footer-nav.col1{left:100px}.footer-nav.col2{left:360px}
.footer-info{position:absolute;left:620px;top:36px;font-size:14px;line-height:1.8}
.footer-brand{width:140px;height:56px;background:var(--white);color:var(--blue);font-weight:900;font-size:28px;letter-spacing:3px;display:flex;align-items:center;justify-content:center;border-radius:6px;margin-bottom:14px}
.copyright{position:absolute;top:3088px;left:0;width:1200px;height:56px;display:flex;align-items:center;justify-content:center;font-size:14px}
</style>
</head>
<body>

<section class="hero">
  <div class="hero-photo" role="img" aria-label="明るいキッチンで鍋を手に料理をする女性の写真"></div>
  <svg class="hero-shape" width="600" height="592" viewBox="0 0 600 592" aria-hidden="true">
    <polygon points="0,130 470,130 0,592" fill="#1cb4e3" opacity=".92"/>
  </svg>
  <div class="hero-copy">
    <p class="hero-label">VISION</p>
    <h1 class="hero-title"><span>ルーチェ・プロダクツの商品が</span><br><span>日々の生活に新提案</span></h1>
  </div>
  <a class="hero-button" href="#">ルーチェ・プロダクツとは</a>
</section>

<header class="site-header">
  <a class="brand" href="#">LUCE</a>
  <nav class="global-nav">
    <a href="#">ルーチェ・プロダクツとは</a>
    <a href="#">商品一覧</a>
    <a href="#">新着情報</a>
    <a href="#">WEBカタログ</a>
    <a href="#">会社案内</a>
  </nav>
  <a class="header-contact" href="#">
    <svg width="52" height="40" viewBox="0 0 52 40" aria-hidden="true"><rect x="2" y="2" width="48" height="36" fill="#fff"/><polyline points="2,2 26,22 50,2" fill="none" stroke="#1cb4e3" stroke-width="3"/></svg>
    お問い合わせ
  </a>
</header>

<section class="products">
  <h2 class="section-title">商品紹介</h2>
  <a class="btn" href="#">商品一覧を見る</a>
  <svg class="arrow prev" viewBox="0 0 36 66" aria-hidden="true"><polygon points="36,0 36,66 0,33" fill="#1cb4e3"/></svg>
  <div class="product-track">
    <div class="product-card">
      <p class="product-cat"><i></i>アイデア商品</p>
      <div class="product-photo" role="img" aria-label="小型の携帯扇風機を持つ手の写真" style="background:linear-gradient(160deg,#cfe3ef,#8fb6cc)"><span class="badge-new">NEW</span></div>
      <p class="product-name">そよかぜハンディファン</p>
    </div>
    <div class="product-card">
      <p class="product-cat"><i></i>キッチン用品</p>
      <div class="product-photo" role="img" aria-label="コンロに置かれた赤い小鍋の写真" style="background:linear-gradient(160deg,#e9e4e0,#b53a30)"></div>
      <p class="product-name">ミニ鍋用コンロスタンド</p>
    </div>
    <div class="product-card">
      <p class="product-cat"><i></i>収納用品</p>
      <div class="product-photo" role="img" aria-label="積み重ねた赤い収納ボックスの写真" style="background:linear-gradient(160deg,#ddd,#c2453d)"></div>
      <p class="product-name">かさねて収納ボックス</p>
    </div>
    <div class="product-card">
      <p class="product-cat"><i></i>生活用品</p>
      <div class="product-photo" role="img" aria-label="窓に貼った断熱シートの写真" style="background:linear-gradient(160deg,#e6e6e6,#9a9a9a)"></div>
      <p class="product-name">ぽかぽか窓 断熱・遮光・保温シート（2枚組）</p>
    </div>
  </div>
  <svg class="arrow next" viewBox="0 0 36 66" aria-hidden="true"><polygon points="0,0 0,66 36,33" fill="#1cb4e3"/></svg>
  <div class="dots"><i></i><i></i><i></i><i></i></div>
</section>

<section class="search">
  <h2><svg width="28" height="28" viewBox="0 0 28 28" aria-hidden="true"><circle cx="11" cy="11" r="8" fill="none" stroke="#fff" stroke-width="4"/><line x1="17" y1="17" x2="26" y2="26" stroke="#fff" stroke-width="4"/></svg>商品検索</h2>
  <div class="search-row">
    <div class="search-input">例）バッグ おにぎり</div>
    <div class="search-submit">検索する</div>
  </div>
</section>

<section class="news">
  <h2 class="section-title">お知らせ</h2>
  <ul class="news-list">
    <li><span class="news-date">2020/11/1</span><span class="news-tag tag-info">お知らせ</span><a class="news-text" href="#">年末年始休業について</a></li>
    <li><span class="news-date">2020/10/23</span><span class="news-tag tag-new">新着情報</span><a class="news-text" href="#">新商品「ひかりワークライト」の発売を開始しました</a></li>
    <li><span class="news-date">2020/10/16</span><span class="news-tag tag-info">お知らせ</span><a class="news-text" href="#">テレビ情報番組「あさのまど」で弊社商品が紹介されました</a></li>
  </ul>
</section>

<section class="info">
  <div class="info-col">
    <h2 class="section-title small">会社案内</h2>
    <div class="info-photo" role="img" aria-label="会社の倉庫と社屋の外観写真" style="background:linear-gradient(180deg,#cfe2f0 0%,#cfe2f0 40%,#b9bcbf 41%,#8e9297 100%)"></div>
    <p class="info-text">ルーチェ・プロダクツ株式会社の会社概要をご覧いただけます。</p>
    <a class="btn" href="#">会社案内を見る</a>
  </div>
  <div class="info-col">
    <h2 class="section-title small">WEBカタログ</h2>
    <div class="info-photo" role="img" aria-label="赤い商品が並ぶカタログ誌面の写真" style="background:linear-gradient(160deg,#f3f3f3,#d44a40)"></div>
    <p class="info-text">WEBで全商品を掲載しております。ご覧いただけます。</p>
    <a class="btn" href="#">WEBカタログを見る</a>
  </div>
  <div class="info-col">
    <h2 class="section-title small">モールショップ</h2>
    <div class="info-photo" role="img" aria-label="オンラインショップ画面を表示したパソコンの写真" style="background:linear-gradient(160deg,#e8f4fa,#9fd3e8)"></div>
    <p class="info-text">弊社商品を直接ご購入いただけます。</p>
    <a class="btn" href="#">ショップを見る</a>
  </div>
</section>

<section class="contact">
  <h2 class="section-title">お問い合わせ</h2>
  <p class="contact-text">商品に関するご不明点についてはよくあるご質問をご覧ください。よくあるご質問に記載以外のご不明点や取材のご依頼等はお問い合わせください。</p>
  <div class="contact-links">
    <a class="btn" href="#">よくあるご質問</a>
    <a class="btn" href="#">お問い合わせ</a>
  </div>
</section>

<footer class="site-footer">
  <ul class="footer-nav col1">
    <li>HOME</li><li>ルーチェ・プロダクツとは</li><li>商品一覧</li><li>新着情報</li><li>WEBカタログ</li><li>会社案内</li>
  </ul>
  <ul class="footer-nav col2">
    <li>お問い合わせ</li><li>よくあるご質問</li><li>リンク</li><li>個人情報保護方針</li><li>サイトマップ</li>
  </ul>
  <div class="footer-info">
    <div class="footer-brand">LUCE</div>
    <p>ルーチェ・プロダクツ株式会社</p>
    <p>〒000-0000</p>
    <p>架空県みどり市中央町1丁目2番3号</p>
    <p>TEL：000-00-0000</p>
    <p>FAX：000-00-0001</p>
  </div>
</footer>
<p class="copyright">© Copyright LUCE PRODUCTS co.,ltd. All Rights Reserved.</p>

</body>
</html>
```